Industrial Services company needs a business card design

We provide industrial maintenance services including sandblasting, painting, pressure washing, storage tank rehabilitation, and welding. I would like an industrial design that's eye catching. I would like the back-side of the card to list our services.

Industry/Entity Type

Construction

Contact Information for Business Card

address: 418 Crestbrook Lane, York, PA 17408
Phone: 410-555-0173
email: velkorinc@mailbox.test
Harold Brennigan, President
www.velkorcoating.test

Logo Text

Velkor Industrial Services

Font styles to use
Sans Serif

Colors
000000
229ed3
0692cd
ffffff

Requirements
Must have
• Easy to read
• our services listed/included on back of card
• eye catching color combinations
Nice to have
• Water storage tank image

```html
<!DOCTYPE html>
<html lang="en">
<head>
<meta charset="utf-8">
<title>Velkor Industrial Services – Business Card</title>
<link rel="stylesheet" href="https://fonts.googleapis.com/css2?family=Lato:wght@400;700;900&display=swap">
<style>
  :root {
    --page-bg: #e6e7e9;
    --card-bg: #ffffff;
    --gear-blue: #0692cd;
    --brand-blue: #229ed3;
    --ink: #222222;
    --on-blue: #ffffff;
  }
  html, body {
    margin: 0;
    width: 1200px;
    height: 900px;
    overflow: hidden;
    background: var(--page-bg);
    font-family: "Lato", Arial, sans-serif;
  }
  .card {
    position: absolute;
    left: 100px;
    top: 141px;
    width: 1000px;
    height: 618px;
    background: var(--card-bg);
    overflow: hidden;
    box-shadow: 0 6px 24px rgba(0,0,0,0.12);
  }
  .gear {
    position: absolute;
    inset: 0;
    width: 1000px;
    height: 618px;
  }
  .gear-shape { fill: var(--gear-blue); }

  .holder { position: absolute; left: 54px; top: 90px; }
  .holder-name {
    margin: 0;
    font-weight: 900;
    font-size: 34px;
    letter-spacing: 0.5px;
    color: var(--brand-blue);
    text-transform: uppercase;
    line-height: 1.1;
  }
  .holder-title {
    margin: 2px 0 0;
    font-size: 27px;
    color: var(--ink);
  }

  .brand {
    position: absolute;
    left: 46px;
    top: 438px;
    display: flex;
    align-items: center;
    gap: 14px;
  }
  .brand-dot {
    width: 26px;
    height: 26px;
    border-radius: 50%;
    background: var(--brand-blue);
  }
  .brand-name {
    font-weight: 900;
    font-size: 31px;
    color: var(--brand-blue);
    white-space: nowrap;
  }

  .contact {
    position: absolute;
    right: 46px;
    top: 150px;
    text-align: right;
    color: var(--on-blue);
    font-size: 27px;
    line-height: 37px;
  }
  .address { margin: 0 0 14px; font-style: normal; }
  .contact-line {
    display: flex;
    justify-content: flex-end;
    align-items: center;
    gap: 8px;
  }
  .contact-line svg { width: 19px; height: 19px; fill: var(--on-blue); }

  .services { position: absolute; right: 46px; top: 368px; text-align: right; color: var(--on-blue); }
  .services-heading {
    margin: 0 0 10px;
    font-size: 24px;
    font-weight: 700;
    text-transform: uppercase;
  }
  .services-list { list-style: none; margin: 0; padding: 0; }
  .services-list li {
    font-size: 21px;
    font-weight: 700;
    text-transform: uppercase;
    line-height: 37.5px;
    display: flex;
    justify-content: flex-end;
    align-items: center;
    gap: 8px;
  }
  .services-list li::after {
    content: "";
    width: 14px;
    height: 14px;
    border-radius: 50%;
    background: var(--on-blue);
  }
</style>
</head>
<body>
  <section class="card">
    <svg class="gear" viewBox="0 0 1000 618" aria-hidden="true">
      <g class="gear-shape" transform="translate(790 330)">
        <circle r="325"/>
        <g>
          <rect x="-34" y="-378" width="68" height="60" transform="rotate(-6)"/>
          <rect x="-34" y="-378" width="68" height="60" transform="rotate(19.7)"/>
          <rect x="-34" y="-378" width="68" height="60" transform="rotate(45.4)"/>
          <rect x="-34" y="-378" width="68" height="60" transform="rotate(71.1)"/>
          <rect x="-34" y="-378" width="68" height="60" transform="rotate(96.8)"/>
          <rect x="-34" y="-378" width="68" height="60" transform="rotate(122.5)"/>
          <rect x="-34" y="-378" width="68" height="60" transform="rotate(148.2)"/>
          <rect x="-34" y="-378" width="68" height="60" transform="rotate(173.9)"/>
          <rect x="-34" y="-378" width="68" height="60" transform="rotate(199.6)"/>
          <rect x="-34" y="-378" width="68" height="60" transform="rotate(225.3)"/>
          <rect x="-34" y="-378" width="68" height="60" transform="rotate(251)"/>
          <rect x="-34" y="-378" width="68" height="60" transform="rotate(276.7)"/>
          <rect x="-34" y="-378" width="68" height="60" transform="rotate(302.4)"/>
          <rect x="-34" y="-378" width="68" height="60" transform="rotate(328.1)"/>
        </g>
      </g>
    </svg>

    <header class="holder">
      <h1 class="holder-name">Harold Brennigan</h1>
      <p class="holder-title">President</p>
    </header>

    <div class="brand">
      <span class="brand-dot"></span>
      <span class="brand-name">Velkor Industrial Services</span>
    </div>

    <div class="contact">
      <address class="address">418 Crestbrook Lane<br>York, PA 17408</address>
      <div class="contact-line">410-555-0173
        <svg viewBox="0 0 20 20" aria-hidden="true"><path d="M2 7c0-3 3-4 8-4s8 1 8 4v2h-4V7H6v2H2z M5 10h10l2 7H3z"/><circle cx="10" cy="13.5" r="2" fill="#0692cd"/></svg>
      </div>
      <div class="contact-line">velkorinc@mailbox.test
        <svg viewBox="0 0 20 20" aria-hidden="true"><path d="M2 4h16v12H2z"/><path d="M3 5l7 6 7-6" fill="none" stroke="#0692cd" stroke-width="1.6"/></svg>
      </div>
      <div class="contact-line">www.velkorcoating.test
        <svg viewBox="0 0 20 20" aria-hidden="true"><circle cx="10" cy="10" r="8.5"/><path d="M10 1.5v17M1.5 10h17M10 1.5c-4 4-4 13 0 17M10 1.5c4 4 4 13 0 17" fill="none" stroke="#0692cd" stroke-width="1.3"/></svg>
      </div>
    </div>

    <section class="services">
      <h2 class="services-heading">Our Services:</h2>
      <ul class="services-list">
        <li>Sandblasting</li>
        <li>Industrial Painting</li>
        <li>Pressure Washing</li>
        <li>Welding</li>
      </ul>
    </section>
  </section>
</body>
</html>
```